Fahrzeugbeschriftung für Software-Dienstleister in der Automation (Robotik)
Zielgruppe
Ich bin freier Softwareentwickler für Industrielle Automationslösungen. Im Klartext bedeutet das, ich schreibe Software für Roboter- und SPS-Steuerungen. Meine Zielgruppe ist sowohl der klassische Maschinenbau (10-500 Mitarbeiter) als auch die Industrie (Automobilbau, Lebensmittelindustrie, Konsumgüter, usw.)
Neben der Softwareentwicklung biete ich meinen Kunden auch Schulungen zum Thema Roboter-Programmierung, sowie Wartung von Industrierobotern an.
Aufgabenstellung
Ich möchte nicht das komplette Fahrzeug als Werbefläche nutzen, das hatte ich bereits in der Vergangenheit. Von meinen Bestandskunden wurde ich zwar auf das Fahrzeug angesprochen, es hat sich jedoch nie ein Neukunde aufgrund der Fahrzeugwerbung gemeldet. Mir geht es vielmehr um einen dezenten, aber dennoch aussagekräftigen Hinweis auf meine Tätigkeiten. Ich stehe mit meinem Fahrzeug regelmäßig bei einem Roboter-Hersteller auf dem Parkplatz, dort laufen täglich mehrere potentielle Kunden direkt an meinem Fahrzeug vorbei. Das heißt, es wird keine Werbung benötigt, die auch bei 50km/h noch zu erkennen ist. Ein Hinweis auf dem Heck würde reichen...
Beim Fahrzeug handelt es sich um den Brenz Valora S-Trim in weiß.
Im Anhang befindet sich das Logo, das aktuelle Design meiner Visitenkarten sowie Bilder (quarzo) vom Fahrzeug, weitere Informationen gibt es auf der Homepage unter www.tk-fertigwerk.net.

```html
<!DOCTYPE html>
<html lang="de">
<head>
<meta charset="utf-8">
<title>tk-fertigwerk – Heckbeschriftung</title>
<link rel="stylesheet" href="https://fonts.googleapis.com/css2?family=Exo+2:wght@400;700&display=swap">
<style>
  :root {
    --paper: #ffffff;
    --lime: #a8c80f;
    --ink: #262626;
    --arm-fill: #ececec;
  }
  html, body {
    margin: 0;
    padding: 0;
    width: 1200px;
    height: 384px;
    overflow: hidden;
    background: var(--paper);
  }
  .rear-label {
    position: relative;
    width: 1200px;
    height: 384px;
    background: var(--paper);
    font-family: "Exo 2", sans-serif;
  }
  .services {
    position: absolute;
    left: 45px;
    top: 76px;
    margin: 0;
    color: var(--lime);
    font-weight: 400;
    font-size: 49px;
    line-height: 64px;
    letter-spacing: 0.2px;
  }
  .web-address {
    position: absolute;
    left: 44px;
    top: 244px;
    margin: 0;
    color: var(--ink);
    font-weight: 700;
    font-size: 84px;
    line-height: 100px;
    letter-spacing: 0.5px;
  }
  .robot-arm {
    position: absolute;
    left: 975px;
    top: 45px;
    width: 180px;
    height: 339px;
  }
</style>
</head>
<body>
  <div class="rear-label">
    <p class="services">Roboter Programmierung |<br>Schulung | Wartung</p>
    <p class="web-address">www.tk-fertigwerk.net</p>
    <svg class="robot-arm" viewBox="0 0 180 339" role="img" aria-label="Strichzeichnung eines Industrieroboter-Arms">
      <rect x="0" y="0" width="180" height="339" rx="14" fill="var(--arm-fill)"/>
    </svg>
  </div>
</body>
</html>
```